Accounting and Financial Services Firm - Modern, Fresh, Original, Professional

We need a business card designed. We would like to see use of the the colors blue. Logo attached.

Modern, Fresh, Original, Professional,
Updates

Email section on business card required. design brief updated.

Target Market(s)

Small to medium businesses and high net worth individuals

Industry/Entity Type

Public Accounting

Contact Information for Business Card

Business Name: PL Ledgerworth Chartered Accountants
Address: Level 9, 42 Garnet Lane Sydney NSW 2000
Ph: 02 9314 2758
Mobile: 04 XXXX XXXX
Email: mara@plledgerworth.com.au
Wechat ID: XXXXXXX
Website: www.plledgerworth.com.au

Name: Mara Osei
Position: Manager

Font styles to use
Sans Serif

Colors
0492cd
33a6d7
85cae6

Requirements
Must have
• Modern font.

```html
<!DOCTYPE html>
<html lang="en">
<head>
<meta charset="utf-8">
<title>PL Ledgerworth – Business Card</title>
<link rel="stylesheet" href="https://fonts.googleapis.com/css2?family=Montserrat:wght@500&family=Roboto:wght@400;500&display=swap">
<style>
  :root {
    --backdrop: #2b2623;
    --card: #1c2025;
    --blue: #0492cd;
    --blue-mid: #33a6d7;
    --blue-light: #85cae6;
    --grey: #a9adb2;
    --white: #f2f4f6;
    --rule: #6b7077;
  }
  * { box-sizing: border-box; margin: 0; padding: 0; }
  html, body { width: 1200px; height: 769px; overflow: hidden; }
  body {
    background: var(--backdrop);
    position: relative;
    font-family: "Roboto", Arial, sans-serif;
  }
  .card {
    position: absolute;
    width: 520px;
    height: 300px;
    background: var(--card);
    border-radius: 4px;
    overflow: hidden;
  }
  .card--front { left: 60px; top: 110px; }
  .card--back { left: 620px; top: 359px; }

  .wordmark {
    display: flex;
    align-items: center;
    gap: 10px;
    font-family: "Montserrat", Arial, sans-serif;
    font-weight: 500;
    color: var(--blue);
    white-space: nowrap;
  }
  .wordmark__square { width: 14px; height: 14px; background: var(--blue); flex: none; }
  .wordmark__text { display: flex; flex-direction: column; line-height: 1.05; }
  .wordmark__name { font-size: 24px; letter-spacing: 0.5px; }
  .wordmark__tagline { font-size: 10px; letter-spacing: 2.2px; text-transform: uppercase; }

  .card--front .wordmark { position: absolute; left: 50%; top: 105px; transform: translateX(-50%); }
  .front__web {
    position: absolute; left: 0; right: 0; top: 196px;
    text-align: center; color: var(--grey);
    font-size: 13px; letter-spacing: 4.5px;
  }

  .card--back .wordmark { position: absolute; right: 40px; top: 58px; }
  .back__person {
    position: absolute; right: 272px; top: 148px;
    text-align: right; color: var(--white); font-size: 13px; line-height: 1.35;
  }
  .back__name { color: var(--blue); font-size: 19px; font-weight: 500; text-transform: uppercase; line-height: 1.1; }
  .back__title { color: var(--grey); font-size: 14px; font-weight: 500; text-transform: uppercase; margin-bottom: 4px; }
  .back__divider {
    position: absolute; left: 264px; top: 150px; width: 1px; height: 112px; background: var(--rule);
  }
  .back__contacts {
    position: absolute; left: 278px; top: 154px;
    list-style: none; color: var(--white); font-size: 14px; line-height: 1;
  }
  .back__contacts li { display: flex; align-items: center; gap: 8px; margin-bottom: 6px; }
  .back__contacts svg { width: 13px; height: 13px; flex: none; fill: var(--blue); }
</style>
</head>
<body>

<section class="card card--front" aria-label="Card front">
  <div class="wordmark">
    <span class="wordmark__square"></span>
    <span class="wordmark__text">
      <span class="wordmark__name">PL LEDGERWORTH</span>
      <span class="wordmark__tagline">Chartered Accountants</span>
    </span>
  </div>
  <p class="front__web">www.plledgerworth.com.au</p>
</section>

<section class="card card--back" aria-label="Card back">
  <div class="wordmark">
    <span class="wordmark__square"></span>
    <span class="wordmark__text">
      <span class="wordmark__name">PL LEDGERWORTH</span>
      <span class="wordmark__tagline">Chartered Accountants</span>
    </span>
  </div>

  <div class="back__person">
    <p class="back__name">Mara Osei</p>
    <p class="back__title">Manager</p>
    <p>Level 9, 42 Garnet Lane</p>
    <p>Sydney NSW 2000</p>
  </div>

  <span class="back__divider"></span>

  <ul class="back__contacts">
    <li>
      <svg viewBox="0 0 16 16" aria-hidden="true"><path d="M3 1h3l1.5 4-2 1.3a9 9 0 0 0 4.2 4.2L11 8.5l4 1.5v3a2 2 0 0 1-2 2A12 12 0 0 1 1 3a2 2 0 0 1 2-2z"/></svg>
      02 9314 2758
    </li>
    <li>
      <svg viewBox="0 0 16 16" aria-hidden="true"><path d="M4 0h8a1 1 0 0 1 1 1v14a1 1 0 0 1-1 1H4a1 1 0 0 1-1-1V1a1 1 0 0 1 1-1zm1 2v10h6V2zm3 11a1 1 0 1 0 0 2 1 1 0 0 0 0-2z"/></svg>
      04 5173 2086
    </li>
    <li>
      <svg viewBox="0 0 16 16" aria-hidden="true"><path d="M8 1c4 0 7 2.6 7 6s-3 6-7 6a8 8 0 0 1-2-.3L2 15l1-3.4A5.7 5.7 0 0 1 1 7c0-3.4 3-6 7-6z"/></svg>
      8305146
    </li>
    <li>
      <svg viewBox="0 0 16 16" aria-hidden="true"><path d="M1 3h14v10H1zm1.5 1.5v.4L8 8.6l5.5-3.7v-.4zm0 2.2v4.8h11V6.7L8 10.4z"/></svg>
      mara@plledgerworth.com.au
    </li>
    <li>
      <svg viewBox="0 0 16 16" aria-hidden="true"><circle cx="8" cy="8" r="7" fill="none" stroke="#0492cd" stroke-width="1.6"/><path d="M1 8h14M8 1c-3 3.5-3 10.5 0 14M8 1c3 3.5 3 10.5 0 14" fill="none" stroke="#0492cd" stroke-width="1.2"/></svg>
      www.plledgerworth.com.au
    </li>
  </ul>
</section>

</body>
</html>
```